Fernlymentor: an app for coaches and students in golf and fitness

I currently have an app that is called Fernlymentor and I am redoing the app completely and with this I am looking for a cool design for the app. I am not happy with the design as it is at the moment. The app should have a nice welcome and when you are logged in the dashboard must be very modern. It is a golf app that have 2 type of users. 1 user is the coach and the other user is the student. Those users can see different things of course.
The coach is normally paying a subscription charge for using the app but I want to get the students to pay for different tools that I will be offering via the app. To me the dashboard and the homepage of the app (once you have downloaded the app) is important. Here I would like to get the student as well as the coach the feeling of what the app can offer. The app offers features like Calendar (here the student can book the coach via the calendar), Chat (here the coach and the student can chat with each other as well as the coach can creat group chats with several students), Notes (here the coach as well as the student can create notes for their lessons), video tips (here the coach can upload video tips for his/her students, online lesson (the student can take online lessons by uploading recorded videos..and so on

Target Market(s)

Sport coaches (for start it will be mostly golf coaches)

Industry/Entity Type

Sports

Font styles to use
Sans Serif

Colors
0054AA
0677BA
7BADD7
CADEEF
E8F1F8

Requirements
Must have
• modern design and easy navigation.
Nice to have
• It all starts with the dashboard
Should not have
• boring standard style.

```html
<!DOCTYPE html>
<html lang="en">
<head>
<meta charset="utf-8">
<title>Fernlymentor – Coach App Screens</title>
<link rel="stylesheet" href="https://fonts.googleapis.com/css2?family=Roboto:wght@400;500;700&display=swap">
<style>
  :root {
    --blue-deep: #0054AA;
    --blue: #0677BA;
    --blue-soft: #7BADD7;
    --blue-light: #CADEEF;
    --blue-pale: #E8F1F8;
    --ink: #1d1d1f;
    --ink-soft: #5b6470;
    --grey-row: #e2e5ea;
    --white: #ffffff;
    --stage: #2f2f2f;
  }
  * { box-sizing: border-box; margin: 0; padding: 0; }
  html, body { width: 1200px; height: 643px; overflow: hidden; }
  body { background: var(--stage); font-family: "Roboto", sans-serif; color: var(--ink); position: relative; }

  .screen { position: absolute; top: 113px; width: 201px; height: 437px; border-radius: 24px; overflow: hidden; background: var(--blue-pale); }
  .screen--dashboard { left: 77px; }
  .screen--agenda { left: 358px; }
  .screen--datepicker { left: 640px; }
  .screen--views { left: 922px; }

  .status { position: absolute; top: 0; left: 0; right: 0; height: 22px; display: flex; justify-content: space-between; align-items: center; padding: 2px 12px 0 11px; font-size: 7px; font-weight: 500; background: var(--white); z-index: 2; }
  .status__icons { display: flex; gap: 3px; align-items: center; }
  .topbar { position: absolute; top: 22px; left: 0; right: 0; height: 35px; background: var(--white); display: flex; align-items: center; justify-content: center; }
  .topbar__title { font-size: 11px; font-weight: 500; }
  .topbar__back { position: absolute; left: 10px; top: 14px; }
  .topbar__menu { position: absolute; right: 11px; top: 9px; width: 18px; height: 18px; border-radius: 50%; background: #e4e6ea; display: flex; align-items: center; justify-content: center; }

  /* Dashboard tiles */
  .tile { position: absolute; width: 85px; height: 93px; background: var(--white); border-radius: 5px; overflow: hidden; }
  .tile--c1 { left: 10px; } .tile--c2 { left: 106px; }
  .tile--r1 { top: 86px; } .tile--r2 { top: 196px; } .tile--r3 { top: 305px; }
  .tile--active { background: linear-gradient(160deg, var(--blue), var(--blue-deep)); color: var(--white); }
  .tile__badge { position: absolute; right: -1px; top: -1px; }
  .tile__title { position: absolute; left: 7px; top: 47px; font-size: 9px; font-weight: 700; white-space: nowrap; }
  .tile__text { position: absolute; left: 7px; top: 64px; right: 5px; font-size: 6px; line-height: 1.55; color: var(--ink-soft); }
  .tile--active .tile__text { color: var(--white); top: 62px; }
  .tile--r2 .tile__title { top: 49px; }
  .tile--r2.tile--c2 .tile__text { top: 66px; }

  /* Agenda */
  .agenda { position: absolute; inset: 0; }
  .agenda__heads { position: absolute; top: 71px; left: 12px; right: 12px; font-size: 7.5px; font-weight: 500; display: flex; }
  .agenda__heads span:first-child { width: 45px; }
  .agenda__expand { position: absolute; right: 10px; top: 70px; }
  .agenda__line { position: absolute; left: 40px; top: 57px; bottom: 33px; width: 1px; background: var(--blue-light); }
  .day { position: absolute; left: 0; right: 0; height: 60px; }
  .day__num { position: absolute; left: 12px; top: 0; width: 20px; text-align: center; font-size: 11px; font-weight: 500; line-height: 1; }
  .day__name { position: absolute; left: 10px; top: 12px; width: 24px; text-align: center; font-size: 7px; color: var(--ink-soft); }
  .day__dot { position: absolute; left: 38px; top: -4px; width: 5px; height: 5px; border-radius: 50%; border: 1px solid var(--blue-light); background: var(--blue-pale); }
  .event { position: absolute; left: 58px; width: 132px; height: 24px; top: -4px; background: var(--grey-row); display: flex; justify-content: space-between; align-items: center; padding: 0 6px 0 8px; font-size: 7.5px; font-weight: 500; white-space: nowrap; }
  .event__time { font-size: 6.5px; }
  .event--current { background: var(--blue); color: var(--white); border: 1px solid var(--blue-light); }
  .booked { position: absolute; left: 58px; width: 132px; height: 20px; top: 29px; background: var(--white); border: 1px solid #dfe3e8; font-size: 6.5px; color: var(--ink-soft); padding: 5px 7px; }
  .day--faded { opacity: .45; }
  .tabbar { position: absolute; left: 0; right: 0; bottom: 0; height: 33px; background: var(--white); display: flex; align-items: center; padding: 0 12px; font-size: 8.5px; font-weight: 500; }
  .tabbar span { margin-right: 15px; }
  .tabbar__right { margin-left: auto; display: flex; }
  .tabbar__right span { margin: 0 0 0 15px; }
  .tabbar__add { position: absolute; left: 84px; top: -9px; width: 32px; height: 32px; border-radius: 50%; background: var(--blue); display: flex; align-items: center; justify-content: center; }

  .dimmed .agenda { filter: blur(1.2px); }
  .scrim { position: absolute; inset: 0; background: rgba(45, 45, 48, .62); }

  /* Date picker */
  .picker { position: absolute; left: 13px; top: 137px; width: 176px; height: 165px; background: var(--white); border-radius: 3px; overflow: hidden; }
  .picker__head { height: 25px; background: var(--blue-deep); color: var(--white); display: flex; align-items: center; justify-content: space-between; padding: 0 7px; font-size: 9.5px; font-weight: 500; }
  .picker__arrow { width: 15px; height: 15px; border-radius: 50%; background: var(--white); display: flex; align-items: center; justify-content: center; }
  .picker__grid { display: grid; grid-template-columns: repeat(7, 1fr); padding: 0 7px; text-align: center; font-size: 7px; }
  .picker__dow { font-size: 5.5px; color: var(--ink-soft); padding: 10px 0 6px; border-bottom: 1px solid #e6e8eb; margin-bottom: 6px; }
  .picker__d { height: 20.5px; line-height: 15px; }
  .picker__d--muted { color: #9aa0a7; }
  .picker__d--sel span { display: inline-block; width: 16px; height: 16px; line-height: 16px; border-radius: 50%; background: var(--blue-deep); color: var(--white); }

  /* View menu */
  .viewmenu { position: absolute; left: 29px; top: 100px; width: 145px; list-style: none; }
  .viewmenu__item { height: 29px; margin-bottom: 13px; border-radius: 15px; background: var(--white); display: flex; align-items: center; justify-content: space-between; padding: 0 12px 0 16px; font-size: 8.5px; font-weight: 500; }
  .viewmenu__item--active { background: var(--blue-deep); color: var(--white); }
</style>
</head>
<body>

<!-- Dashboard -->
<section class="screen screen--dashboard">
  <div class="status"><span>12:00 ↗</span><span class="status__icons"><svg width="9" height="5"><rect x="0" y="3" width="1.5" height="2"/><rect x="2.5" y="2" width="1.5" height="3"/><rect x="5" y="1" width="1.5" height="4"/><rect x="7.5" y="0" width="1.5" height="5"/></svg><svg width="12" height="6"><rect x=".5" y=".5" width="10" height="5" rx="1" fill="none" stroke="#000"/><rect x="1.5" y="1.5" width="8" height="3"/></svg></span></div>
  <header class="topbar">
    <svg class="topbar__back" width="12" height="7"><path d="M1 3.5h11M4 .5L1 3.5l3 3" stroke="#111" stroke-width="1.3" fill="none"/></svg>
    <h1 class="topbar__title">Dashboard</h1>
    <span class="topbar__menu"><svg width="7" height="6"><path d="M0 .5h7M0 3h7M0 5.5h7" stroke="#111" stroke-width="1"/></svg></span>
  </header>

  <article class="tile tile--c1 tile--r1">
    <svg class="tile__badge" width="42" height="42"><circle cx="42" cy="0" r="41" fill="var(--blue-soft)"/><circle cx="42" cy="0" r="34" fill="var(--blue)"/><circle cx="42" cy="0" r="26" fill="var(--blue-deep)"/><rect x="18" y="8" width="16" height="14" rx="2" fill="#fff"/><g fill="var(--blue-deep)"><rect x="20" y="13" width="3" height="2"/><rect x="24.5" y="13" width="3" height="2"/><rect x="29" y="13" width="3" height="2"/><rect x="20" y="17" width="3" height="2"/><rect x="24.5" y="17" width="3" height="2"/><rect x="29" y="17" width="3" height="2"/></g></svg>
    <h2 class="tile__title">My Calendar</h2>
    <p class="tile__text">Book and manage your appointments 24/7</p>
  </article>

  <article class="tile tile--c2 tile--r1">
    <svg class="tile__badge" width="42" height="42"><circle cx="42" cy="0" r="41" fill="var(--blue-soft)"/><circle cx="42" cy="0" r="34" fill="var(--blue)"/><circle cx="42" cy="0" r="26" fill="var(--blue-deep)"/><rect x="17" y="6" width="20" height="14" rx="1" fill="#fff"/><circle cx="27" cy="15" r="3" fill="none" stroke="var(--blue-deep)" stroke-width="1"/><path d="M27 20v4" stroke="#fff" stroke-width="1"/></svg>
    <h2 class="tile__title">Online Lessons</h2>
    <p class="tile__text">Edit and view your students online lessons</p>
  </article>

  <article class="tile tile--c1 tile--r2 tile--active">
    <svg class="tile__badge" width="42" height="42" role="img" aria-label="Product mark placeholder"><circle cx="42" cy="0" r="41" fill="var(--blue-light)"/><circle cx="42" cy="0" r="34" fill="var(--blue-pale)"/><circle cx="42" cy="0" r="26" fill="#fff"/><circle cx="28" cy="14" r="6" fill="var(--blue-deep)"/></svg>
    <h2 class="tile__title">My Products</h2>
    <p class="tile__text">Configure lessons detail for calendar and online lesson</p>
  </article>

  <article class="tile tile--c2 tile--r2">
    <svg class="tile__badge" width="42" height="42"><circle cx="42" cy="0" r="41" fill="var(--blue-soft)"/><circle cx="42" cy="0" r="34" fill="var(--blue)"/><circle cx="42" cy="0" r="26" fill="var(--blue-deep)"/><path d="M21 8l7-3 7 3-7 3z" fill="#fff"/><circle cx="28" cy="14" r="3.5" fill="#fff"/><path d="M20 24c0-5 4-6 8-6s8 1 8 6z" fill="#fff"/></svg>
    <h2 class="tile__title">My Students</h2>
    <p class="tile__text">Find all info of your students</p>
  </article>

  <article class="tile tile--c1 tile--r3">
    <svg class="tile__badge" width="42" height="42"><circle cx="42" cy="0" r="41" fill="var(--blue-soft)"/><circle cx="42" cy="0" r="34" fill="var(--blue)"/><circle cx="42" cy="0" r="26" fill="var(--blue-deep)"/><rect x="18" y="5" width="12" height="9" fill="none" stroke="#fff" stroke-width="1"/><path d="M19 17v6M22 17v6M25 17v6" stroke="#fff" stroke-width="1.2"/><circle cx="32" cy="19" r="4" fill="#fff"/><path d="M31 17v4l3-2z" fill="var(--blue-deep)"/></svg>
    <h2 class="tile__title">Video Editor</h2>
    <p class="tile__text">Book and manage your appointments 24/7</p>
  </article>

  <article class="tile tile--c2 tile--r3">
    <svg class="tile__badge" width="42" height="42"><circle cx="42" cy="0" r="41" fill="var(--blue-soft)"/><circle cx="42" cy="0" r="34" fill="var(--blue)"/><circle cx="42" cy="0" r="26" fill="var(--blue-deep)"/><path d="M27 5v16" stroke="#fff" stroke-width="1.4"/><path d="M27 5l7 3-7 3z" fill="#fff"/><ellipse cx="27" cy="22" rx="8" ry="2.5" fill="#fff"/></svg>
    <h2 class="tile__title">Fernly365</h2>
    <p class="tile__text">Book and manage your appointments 24/7</p>
  </article>
</section>

<!-- Agenda week list -->
<section class="screen screen--agenda">
  <div class="agenda">
    <div class="status"><span>12:00 ↗</span><span class="status__icons"><svg width="9" height="5"><rect x="0" y="3" width="1.5" height="2"/><rect x="2.5" y="2" width="1.5" height="3"/><rect x="5" y="1" width="1.5" height="4"/><rect x="7.5" y="0" width="1.5" height="5"/></svg><svg width="12" height="6"><rect x=".5" y=".5" width="10" height="5" rx="1" fill="none" stroke="#000"/><rect x="1.5" y="1.5" width="8" height="3"/></svg></span></div>
    <header class="topbar">
      <svg class="topbar__back" width="12" height="7"><path d="M1 3.5h11M4 .5L1 3.5l3 3" stroke="#111" stroke-width="1.3" fill="none"/></svg>
      <h1 class="topbar__title">April 17-22, 2022</h1>
      <span class="topbar__menu"><svg width="7" height="6"><path d="M0 .5h7M0 3h7M0 5.5h7" stroke="#111" stroke-width="1"/></svg></span>
    </header>
    <div class="agenda__line"></div>
    <div class="agenda__heads"><span>DATE</span><span>EVENTS</span></div>
    <svg class="agenda__expand" width="10" height="10"><path d="M0 3V0h3M7 0h3v3M10 7v3H7M3 10H0V7" stroke="#444" fill="none"/><circle cx="5" cy="5" r="2" fill="none" stroke="#444"/></svg>
    <div class="day" style="top:102px"><span class="day__num">17</span><span class="day__name">SAT</span><span class="day__dot"></span><div class="event event--current"><span>My FlatRate lesson3</span><span class="event__time">8.30 - 9.30</span></div><div class="booked">Booked: 0 of 10</div></div>
    <div class="day" style="top:173px"><span class="day__num">18</span><span class="day__name">SUN</span><span class="day__dot"></span><div class="event"><span>My FlatRate lesson3</span><span class="event__time">8.00 - 9.00</span></div><div class="booked">Booked: 0 of 10</div></div>
    <div class="day" style="top:244px"><span class="day__num">19</span><span class="day__name">MON</span><span class="day__dot"></span><div class="event"><span>My FlatRate lesson3</span><span class="event__time">8.00 - 9.00</span></div><div class="booked">Booked: 0 of 10</div></div>
    <div class="day" style="top:315px"><span class="day__num">20</span><span class="day__name">TUE</span><span class="day__dot"></span><div class="event"><span>My FlatRate lesson3</span><span class="event__time">8.00 - 9.00</span></div><div class="booked">Booked: 0 of 10</div></div>
    <div class="day day--faded" style="top:386px"><span class="day__num">21</span><span class="day__name">WEN</span><span class="day__dot"></span><div class="event"><span>My FlatRate lesson3</span><span class="event__time">8.00 - 9.00</span></div></div>
    <nav class="tabbar"><span>Views</span><span>Date</span><a class="tabbar__add"><svg width="11" height="11"><path d="M5.5 0v11M0 5.5h11" stroke="#fff" stroke-width="2"/></svg></a><div class="tabbar__right"><span>Setting</span><span>Next</span></div></nav>
  </div>
</section>

<!-- Date picker -->
<section class="screen screen--datepicker dimmed">
  <div class="agenda">
    <div class="status"><span>12:00 ↗</span><span class="status__icons"></span></div>
    <header class="topbar"><h1 class="topbar__title">April 17-22, 2022</h1></header>
    <div class="agenda__line"></div>
    <div class="agenda__heads"><span>DATE</span><span>EVENTS</span></div>
    <div class="day" style="top:102px"><span class="day__num">17</span><span class="day__name">SAT</span><div class="event event--current"><span>My FlatRate lesson3</span><span class="event__time">8.30 - 9.30</span></div></div>
    <div class="day" style="top:315px"><span class="day__num">20</span><span class="day__name">TUE</span><div class="event"><span>My FlatRate lesson3</span><span class="event__time">8.00 - 9.00</span></div><div class="booked">Booked: 0 of 10</div></div>
    <div class="day day--faded" style="top:386px"><span class="day__num">21</span><span class="day__name">WEN</span><div class="event"><span>My FlatRate lesson3</span><span class="event__time">8.00 - 9.00</span></div></div>
    <nav class="tabbar"><span>Views</span><span>Date</span><a class="tabbar__add"><svg width="11" height="11"><path d="M5.5 0v11M0 5.5h11" stroke="#fff" stroke-width="2"/></svg></a><div class="tabbar__right"><span>Setting</span><span>Next</span></div></nav>
  </div>
  <div class="scrim"></div>
  <div class="picker">
    <div class="picker__head">
      <span class="picker__arrow"><svg width="5" height="7"><path d="M4 .5L1 3.5l3 3" stroke="var(--blue-deep)" stroke-width="1.3" fill="none"/></svg></span>
      <span>May 2021</span>
      <span class="picker__arrow"><svg width="5" height="7"><path d="M1 .5l3 3-3 3" stroke="var(--blue-deep)" stroke-width="1.3" fill="none"/></svg></span>
    </div>
    <div class="picker__grid">
      <span class="picker__dow">MON</span><span class="picker__dow">TUE</span><span class="picker__dow">WED</span><span class="picker__dow">THU</span><span class="picker__dow">FRI</span><span class="picker__dow">SAT</span><span class="picker__dow">SUN</span>
      <span class="picker__d picker__d--muted">28</span><span class="picker__d picker__d--muted">29</span><span class="picker__d picker__d--muted">30</span><span class="picker__d picker__d--muted">31</span><span class="picker__d">1</span><span class="picker__d">2</span><span class="picker__d">3</span>
      <span class="picker__d">4</span><span class="picker__d">5</span><span class="picker__d">6</span><span class="picker__d">7</span><span class="picker__d">8</span><span class="picker__d">9</span><span class="picker__d">10</span>
      <span class="picker__d">11</span><span class="picker__d">12</span><span class="picker__d">13</span><span class="picker__d">14</span><span class="picker__d">15</span><span class="picker__d">16</span><span class="picker__d picker__d--sel"><span>17</span></span>
      <span class="picker__d">18</span><span class="picker__d">19</span><span class="picker__d">20</span><span class="picker__d">21</span><span class="picker__d">22</span><span class="picker__d">23</span><span class="picker__d">24</span>
      <span class="picker__d">25</span><span class="picker__d">26</span><span class="picker__d">27</span><span class="picker__d">28</span><span class="picker__d">29</span><span class="picker__d">30</span><span class="picker__d picker__d--muted">1</span>
    </div>
  </div>
</section>

<!-- View selector -->
<section class="screen screen--views dimmed">
  <div class="agenda">
    <div class="status"><span>12:00 ↗</span><span class="status__icons"></span></div>
    <header class="topbar"><h1 class="topbar__title">April 17-22, 2022</h1></header>
    <div class="agenda__line"></div>
    <div class="agenda__heads"><span>DATE</span><span>EVENTS</span></div>
    <div class="day" style="top:102px"><span class="day__num">17</span><span class="day__name">SAT</span><div class="event event--current"><span>My FlatRate lesson3</span><span class="event__time">8.30 - 9.30</span></div><div class="booked">Booked: 0 of 10</div></div>
    <div class="day" style="top:173px"><span class="day__num">18</span><span class="day__name">SUN</span><div class="event"><span>My FlatRate lesson3</span><span class="event__time">8.00 - 9.00</span></div><div class="booked">Booked: 0 of 10</div></div>
    <div class="day" style="top:244px"><span class="day__num">19</span><span class="day__name">MON</span><div class="event"><span>My FlatRate lesson3</span><span class="event__time">8.00 - 9.00</span></div><div class="booked">Booked: 0 of 10</div></div>
    <div class="day" style="top:315px"><span class="day__num">20</span><span class="day__name">TUE</span><div class="event"><span>My FlatRate lesson3</span><span class="event__time">8.00 - 9.00</span></div><div class="booked">Booked: 0 of 10</div></div>
    <nav class="tabbar"><span>Views</span><span>Date</span><a class="tabbar__add"><svg width="11" height="11"><path d="M5.5 0v11M0 5.5h11" stroke="#fff" stroke-width="2"/></svg></a><div class="tabbar__right"><span>Setting</span><span>Next</span></div></nav>
  </div>
  <div class="scrim"></div>
  <ul class="viewmenu">
    <li class="viewmenu__item viewmenu__item--active">MONTH<svg width="6" height="9"><path d="M1 1l4 3.5-4 3.5" stroke="#fff" stroke-width="1.4" fill="none"/></svg></li>
    <li class="viewmenu__item">WEEK<svg width="6" height="9"><path d="M1 1l4 3.5-4 3.5" stroke="#111" stroke-width="1.4" fill="none"/></svg></li>
    <li class="viewmenu__item">3- DAYS<svg width="6" height="9"><path d="M1 1l4 3.5-4 3.5" stroke="#111" stroke-width="1.4" fill="none"/></svg></li>
    <li class="viewmenu__item">DAY<svg width="6" height="9"><path d="M1 1l4 3.5-4 3.5" stroke="#111" stroke-width="1.4" fill="none"/></svg></li>
    <li class="viewmenu__item">TODAY<svg width="6" height="9"><path d="M1 1l4 3.5-4 3.5" stroke="#111" stroke-width="1.4" fill="none"/></svg></li>
    <li class="viewmenu__item">LIST<svg width="6" height="9"><path d="M1 1l4 3.5-4 3.5" stroke="#111" stroke-width="1.4" fill="none"/></svg></li>
  </ul>
</section>

</body>
</html>
```